The Radiant Scroll of Petitions, Steadfast Petitions Across Seasons of Trial

I want a book cover design, The book is a prayer book. Pleas no design with only words. I want something creative and original. Something that attracts attention just by looking at the cover. Something powerful. This book is for people that are experiencing issues and need prayer. This book is also for those that want to pray and pray effectively. Not only will there be prayers. But they will learn the dynamics of prayer and how to pray effectively and from the right position. This book is filled with power yet effective prayers that will.have the ability to break bondages off people lives.
Below is some book covers that I found. I posted them to give an idea of what im looking for. Something that catches the attention of a reader.

Target Market(s)

Everyone, religious people

Industry/Entity Type

Religious

Font styles to use
Serif
Sans Serif

Requirements
Must have
• Creativity, originality,
Nice to have
• Professional looking. Powerful looking
Should not have
• Should not have just one color with big ole words across the whole book.

```html
<!DOCTYPE html>
<html lang="en">
<head>
<meta charset="utf-8">
<title>The Radiant Scroll of Petitions — Cover Layout</title>
<link rel="stylesheet" href="https://fonts.googleapis.com/css2?family=Sansita+Swashed:wght@400;500&family=Ubuntu:wght@300;400&display=swap">
<style>
  :root {
    --stage: #c2b49a;
    --label: #8a7d68;
    --guide: #ffffff;
    --back-dark: #070707;
    --back-mid: #1a1a1a;
    --teal-dark: #0f2a2c;
    --ember: #c4452a;
    --glow: #ffe9a8;
    --sand: #b9673e;
    --title-red: #8c1f1f;
    --ink-light: #ffffff;
    --body-light: #e8e8e8;
  }
  * { margin: 0; padding: 0; box-sizing: border-box; }
  html, body { width: 1200px; height: 915px; overflow: hidden; background: var(--stage); }
  .canvas { position: relative; width: 1200px; height: 915px; }

  .cover {
    position: absolute; left: 117px; top: 111px; width: 967px; height: 693px;
    box-shadow: 6px 6px 8px rgba(0,0,0,0.35);
  }
  .back-cover {
    position: absolute; left: 0; top: 0; width: 461px; height: 693px;
    background: linear-gradient(160deg, var(--back-mid) 0%, var(--back-dark) 45%, #000 100%);
  }
  .front-photo {
    position: absolute; left: 461px; top: 0; width: 506px; height: 693px;
    background:
      radial-gradient(ellipse 110px 140px at 391px 405px, var(--glow) 0%, #f5b54a 35%, rgba(230,110,40,0.7) 60%, rgba(0,0,0,0) 100%),
      radial-gradient(ellipse 200px 300px at 391px 430px, rgba(196,69,42,0.85) 0%, rgba(196,69,42,0) 100%),
      linear-gradient(180deg, var(--teal-dark) 0%, #1d2b28 40%, #5a3020 68%, var(--sand) 85%, #6b3a22 100%);
  }

  .author-photo {
    position: absolute; left: 31px; top: 287px; width: 120px; height: 120px;
    border: 1px solid #cfcfcf;
    display: flex; align-items: center; justify-content: center;
    font-family: "Ubuntu", sans-serif; font-weight: 300; font-size: 25px; color: var(--ink-light);
  }
  .author-name {
    position: absolute; left: 161px; top: 376px;
    font-family: "Ubuntu", sans-serif; font-weight: 300; font-size: 19px; color: var(--ink-light); line-height: 1;
  }
  .author-role {
    position: absolute; left: 161px; top: 398px;
    font-family: "Ubuntu", sans-serif; font-weight: 300; font-size: 8.5px; color: var(--body-light);
  }
  .blurb {
    position: absolute; left: 31px; top: 436px; width: 402px;
    font-family: "Ubuntu", sans-serif; font-weight: 300; font-size: 8.4px; line-height: 11.5px; color: var(--body-light);
  }
  .blurb p + p { margin-top: 11px; }

  .spine-text {
    position: absolute; left: 472px; top: 250px; width: 26px; height: 420px;
    writing-mode: vertical-rl; transform: rotate(180deg);
    display: flex; align-items: center; gap: 9px;
    color: var(--ink-light); white-space: nowrap;
  }
  .spine-author { font-family: "Ubuntu", sans-serif; font-weight: 300; font-size: 17px; }
  .spine-divider { font-family: "Ubuntu", sans-serif; font-weight: 300; font-size: 15px; }
  .spine-title { font-family: "Sansita Swashed", cursive; font-size: 20px; }

  .front-title {
    position: absolute; left: 621px; top: 378px; width: 230px;
    text-align: center; font-family: "Sansita Swashed", cursive; font-weight: 500;
    font-size: 25px; line-height: 34px; color: var(--title-red);
  }
  .front-subtitle {
    position: absolute; left: 461px; top: 652px; width: 506px;
    text-align: center; font-family: "Sansita Swashed", cursive; font-size: 19px; color: var(--ink-light);
  }

  .guides { position: absolute; left: 0; top: 0; }

  .label {
    position: absolute; font-family: "Ubuntu", sans-serif; font-weight: 300; font-size: 17px; color: var(--label);
  }
  .label-back { left: 310px; top: 825px; }
  .label-front { left: 810px; top: 825px; }
  .label-spine { left: 592px; top: 826px; writing-mode: vertical-rl; transform: rotate(180deg); }
</style>
</head>
<body>
<div class="canvas">
  <div class="cover">
    <div class="back-cover" role="img" aria-label="Dark night sand dunes with wind ripples and faint speckles"></div>
    <div class="front-photo" role="img" aria-label="Glowing red oil lantern resting in sand at night, lit from within"></div>

    <div class="author-photo">Picture</div>
    <div class="author-name">Author’s name</div>
    <div class="author-role">Author’s title/function/ocupation</div>
    <div class="blurb">
      <p>Every prayer begins with a quiet step toward the light. In these pages you will find words for the hours when strength runs thin and the road seems long. Each petition is written to be spoken aloud, in faith, from the right position before God. Learn how prayer moves, how it is heard, and how it breaks the chains that hold a life back from freedom.</p>
      <p>Written for anyone walking through a season of trial, this book gathers steadfast petitions for healing, provision, protection and peace. Beside each prayer you will find a short teaching on the dynamics of prayer: why persistence matters, how scripture shapes our asking, and what it means to stand with authority. Use it alone in the early morning, with family at the table, or with a small group that meets to intercede. Keep it close, return to it often, and let its pages become a lamp that steadies your steps until the night gives way to morning once more.</p>
    </div>

    <div class="spine-text">
      <span class="spine-author">Author’s name</span>
      <span class="spine-divider">|</span>
      <span class="spine-title">The Radiant Scroll of Petitions</span>
    </div>

    <div class="front-title">The<br>Radiant Scroll<br>of Petitions</div>
    <div class="front-subtitle">Steadfast Petitions Across Seasons of Trial</div>
  </div>

  <svg class="guides" width="1200" height="915" aria-hidden="true">
    <line x1="578" y1="74" x2="578" y2="852" stroke="var(--guide)" stroke-width="1.2" stroke-dasharray="8 4"/>
    <line x1="623" y1="74" x2="623" y2="852" stroke="var(--guide)" stroke-width="1.2" stroke-dasharray="8 4"/>
  </svg>

  <div class="label label-back">back cover</div>
  <div class="label label-spine">spine</div>
  <div class="label label-front">front cover</div>
</div>
</body>
</html>
```